Kestrel Bridge Consulting (KBC) Business Card Design

I would like to create double-sided business cards that contain:
1) Name: Derek Molvane
2) Phone Number: +1 (555) 218-4907
3) Email: Derek.Molvane@KestrelBridgeConsulting.example
4) Website: KestrelBridgeConsulting.example

I would like to include my logo and a color scheme similar to the Varnholt Grand Prix Ostera squad color scheme (black, silver, greenish-blue – but can also include regular blue)

What we do: Our company develops and delivers innovative and pragmatic information technology and cybersecurity risk and compliance solutions for organizations in the commercial market as well as the federal, and state/local sectors.

```html
<!DOCTYPE html>
<html lang="en">
<head>
<meta charset="utf-8">
<title>Kestrel Bridge Consulting – Business Card</title>
<link href="https://fonts.googleapis.com/css2?family=Noto+Sans:wght@400;700&display=swap" rel="stylesheet">
<style>
  :root {
    --backdrop: #d9d6d2;
    --card-dark: #2a2a2a;
    --card-light: #f0eff4;
    --brand-blue: #1a73e8;
    --brand-cyan: #16b4f0;
    --ink: #333338;
    --ink-light: #e9e9ee;
    --shadow: rgba(0,0,0,0.22);
  }
  * { margin: 0; padding: 0; box-sizing: border-box; }
  html, body { width: 1200px; height: 901px; overflow: hidden; }
  body {
    background: var(--backdrop);
    font-family: "Noto Sans", Arial, sans-serif;
    position: relative;
  }
  .card {
    position: absolute;
    top: 302px;
    width: 520px;
    height: 297px;
    box-shadow: 0 10px 26px var(--shadow);
  }
  .card--back { left: 60px; background: var(--card-dark); }
  .card--front { left: 620px; background: var(--card-light); }

  .brand {
    position: absolute;
    display: flex;
    align-items: center;
    gap: 14px;
  }
  .card--back .brand { left: 50%; top: 50%; transform: translate(-50%, -50%); }
  .card--front .brand { left: 118px; top: 58px; }
  .brand__dot {
    width: 54px; height: 54px;
    border-radius: 50%;
    background: var(--brand-cyan);
    flex: none;
  }
  .brand__name {
    font-weight: 700;
    font-size: 17px;
    line-height: 1.05;
    letter-spacing: 2px;
    text-transform: uppercase;
  }
  .card--back .brand__name { color: var(--ink-light); }
  .card--front .brand__name { color: var(--ink); }

  .contact {
    position: absolute;
    left: 70px;
    top: 168px;
  }
  .contact__name {
    font-weight: 700;
    font-size: 27px;
    color: var(--brand-blue);
    line-height: 1.1;
  }
  .contact__role {
    font-size: 11px;
    color: var(--ink);
    margin-top: 2px;
  }
  .contact__rule {
    width: 34px; height: 3px;
    background: var(--brand-blue);
    margin: 4px 0 9px;
  }
  .contact__list { list-style: none; }
  .contact__item {
    display: flex;
    align-items: center;
    gap: 8px;
    font-size: 11px;
    color: var(--ink);
    line-height: 1.65;
  }
  .contact__icon { width: 11px; height: 11px; flex: none; fill: var(--brand-blue); }
</style>
</head>
<body>
  <section class="card card--back" aria-label="Card back">
    <div class="brand">
      <span class="brand__dot"></span>
      <span class="brand__name">Kestrel<br>Bridge<br>Consulting</span>
    </div>
  </section>

  <section class="card card--front" aria-label="Card front">
    <div class="brand">
      <span class="brand__dot"></span>
      <span class="brand__name">Kestrel<br>Bridge<br>Consulting</span>
    </div>

    <div class="contact">
      <h1 class="contact__name">Derek Molvane</h1>
      <p class="contact__role">Manager</p>
      <div class="contact__rule"></div>
      <ul class="contact__list">
        <li class="contact__item">
          <svg class="contact__icon" viewBox="0 0 24 24" aria-hidden="true"><path d="M6.6 10.8a15.1 15.1 0 0 0 6.6 6.6l2.2-2.2a1 1 0 0 1 1-.25 11.4 11.4 0 0 0 3.6.57 1 1 0 0 1 1 1V20a1 1 0 0 1-1 1A17 17 0 0 1 3 4a1 1 0 0 1 1-1h3.5a1 1 0 0 1 1 1c0 1.25.2 2.45.57 3.6a1 1 0 0 1-.25 1z"/></svg>
          +1 (555) 218-4907
        </li>
        <li class="contact__item">
          <svg class="contact__icon" viewBox="0 0 24 24" aria-hidden="true"><path d="M2 5h20v14H2z M2 5l10 8 10-8" fill="none" stroke="var(--brand-blue)" stroke-width="2.4"/></svg>
          Derek.Molvane@KestrelBridgeConsulting.example
        </li>
        <li class="contact__item">
          <svg class="contact__icon" viewBox="0 0 24 24" aria-hidden="true"><g fill="none" stroke="var(--brand-blue)" stroke-width="2"><circle cx="12" cy="12" r="10"/><ellipse cx="12" cy="12" rx="4.5" ry="10"/><path d="M2 12h20"/></g></svg>
          KestrelBridgeConsulting.example
        </li>
      </ul>
    </div>
  </section>
</body>
</html>
```